Cryptocurrency Advisor Business Card

Dravelin Consulting Services is my company, which advises many projects in the ICO/Cryptocurrency industry. I'd like to get a sleek, preferably matte black or matte dark blue finish, business card with the company name (and simple logo w/ crypto feel) on one side and while the other side I'd like a small twitter and telegram logo together maybe separated by a / as it's the same, then an email and a phone logo so I can insert those specifics there (no address). Can have name then CEO section too. At the bottom of that section, find a place for more of a job description: ICO Advisor, World Champion Gamer, Esports Award Winner, Quorvane Expert. You can possibly design a simple logo or use something with a crypto twist or background, but nothing too complex. Rounded edges for printing not square.
Updates

Had personal issues taking a few days away from me being able to provide feedback and check designs, etc. Will be more active now finalizing design just needed few days from issue but all is sorted.

Target Market(s)

Cryptocurrency industry

Industry/Entity Type

Management Consulting

Contact Information for Business Card

Font styles to use
Sans Serif

Colors
5c5c5c
474747
757575
9d9d9d
aaaaaa
333333
0355a3

Requirements
Must have
• Refer to Details/Description
Nice to have
Should not have
• Address section

```html
<!DOCTYPE html>
<html lang="en">
<head>
<meta charset="utf-8">
<title>Dravelin Consulting Services – Business Card</title>
<link rel="stylesheet" href="https://fonts.googleapis.com/css2?family=Roboto:wght@300;400;500;700&display=swap">
<style>
  :root {
    --canvas: #e4e4e4;
    --paper: #ffffff;
    --ink-dark: #333333;
    --ink-deep: #242424;
    --ink-mid: #474747;
    --ink-soft: #9d9d9d;
    --brand-blue: #0355a3;
    --text-light: #ffffff;
    --text-muted: #aaaaaa;
  }
  * { box-sizing: border-box; margin: 0; padding: 0; }
  html, body {
    width: 1200px;
    height: 794px;
    overflow: hidden;
    background: var(--canvas);
    font-family: "Roboto", Arial, sans-serif;
  }
  .canvas {
    position: relative;
    width: 1200px;
    height: 794px;
  }
  .card {
    position: absolute;
    top: 242px;
    width: 540px;
    height: 309px;
    border-radius: 22px;
    overflow: hidden;
    box-shadow: 0 10px 28px rgba(0,0,0,0.18);
  }
  .card-front { left: 40px; }
  .card-back  { left: 620px; }
  .card-bg {
    position: absolute;
    inset: 0;
    width: 100%;
    height: 100%;
  }

  /* Front: company name */
  .brand {
    position: absolute;
    top: 58px;
    left: 0;
    width: 100%;
    display: flex;
    justify-content: center;
    align-items: center;
    gap: 10px;
  }
  .brand-mark {
    width: 16px;
    height: 16px;
    background: var(--brand-blue);
  }
  .brand-name {
    font-weight: 500;
    font-size: 22px;
    color: var(--brand-blue);
    letter-spacing: 0.5px;
  }

  /* Front: name block */
  .holder {
    position: absolute;
    left: 24px;
    top: 180px;
    color: var(--text-light);
  }
  .holder-name {
    font-weight: 700;
    font-size: 24px;
    line-height: 28px;
  }
  .holder-title {
    font-weight: 500;
    font-size: 9px;
    letter-spacing: 0.5px;
    margin-top: 2px;
  }

  /* Front: roles */
  .roles {
    position: absolute;
    left: 24px;
    top: 236px;
    list-style: none;
    color: var(--text-light);
    font-weight: 300;
    font-size: 14px;
    line-height: 17px;
  }

  /* Front: contacts */
  .contacts {
    position: absolute;
    left: 318px;
    top: 162px;
    list-style: none;
    color: var(--text-light);
    font-weight: 400;
    font-size: 12px;
  }
  .contacts li {
    display: flex;
    align-items: center;
    gap: 8px;
    height: 21px;
  }
  .contact-icon {
    display: flex;
    gap: 3px;
    align-items: center;
    width: 34px;
    color: var(--text-muted);
    font-size: 11px;
  }
  .social-dot {
    width: 11px;
    height: 11px;
    border-radius: 50%;
    background: var(--text-muted);
  }
  .contact-icon svg { width: 12px; height: 12px; }

  /* Back */
  .back-brand {
    position: absolute;
    inset: 0;
    display: flex;
    justify-content: center;
    align-items: center;
    gap: 14px;
  }
  .back-brand .brand-mark { width: 22px; height: 22px; }
  .back-brand .brand-name { font-size: 30px; }
</style>
</head>
<body>
<main class="canvas">

  <section class="card card-front" aria-label="Business card front">
    <svg class="card-bg" viewBox="0 0 540 309" preserveAspectRatio="none" aria-hidden="true">
      <rect width="540" height="309" fill="var(--ink-dark)"/>
      <polygon points="0,0 540,0 540,134 296,134 262,168 0,168" fill="var(--paper)"/>
      <polygon points="0,168 262,168 296,134 540,134 540,150 304,150 272,182 272,228 0,228" fill="var(--brand-blue)"/>
      <line x1="272" y1="228" x2="272" y2="309" stroke="var(--ink-mid)" stroke-width="1"/>
    </svg>

    <div class="brand">
      <span class="brand-mark"></span>
      <span class="brand-name">Dravelin Consulting Services</span>
    </div>

    <div class="holder">
      <p class="holder-name">Your Name Here</p>
      <p class="holder-title">CEO</p>
    </div>

    <ul class="roles">
      <li>ICO Advisor</li>
      <li>World Champion Gamer</li>
      <li>Esports Award Winner</li>
      <li>Quorvane Expert</li>
    </ul>

    <ul class="contacts">
      <li>
        <span class="contact-icon"><span class="social-dot"></span>/<span class="social-dot"></span></span>
        <span>@yourusername</span>
      </li>
      <li>
        <span class="contact-icon">
          <svg viewBox="0 0 24 24"><path fill="currentColor" d="M6.6 10.8a15.1 15.1 0 0 0 6.6 6.6l2.2-2.2a1 1 0 0 1 1-.25 11.4 11.4 0 0 0 3.6.57 1 1 0 0 1 1 1V20a1 1 0 0 1-1 1A17 17 0 0 1 3 4a1 1 0 0 1 1-1h3.5a1 1 0 0 1 1 1c0 1.25.2 2.45.57 3.57a1 1 0 0 1-.25 1z"/></svg>
        </span>
        <span>(00) 0000 0000</span>
      </li>
      <li>
        <span class="contact-icon">
          <svg viewBox="0 0 24 24"><rect x="6" y="2" width="12" height="20" rx="2" fill="none" stroke="currentColor" stroke-width="2"/><circle cx="12" cy="18" r="1.2" fill="currentColor"/></svg>
        </span>
        <span>(00) 0000 0000</span>
      </li>
      <li>
        <span class="contact-icon">@</span>
        <span>yourname@mailvane.com</span>
      </li>
    </ul>
  </section>

  <section class="card card-back" aria-label="Business card back">
    <svg class="card-bg" viewBox="0 0 540 309" preserveAspectRatio="none" aria-hidden="true">
      <defs>
        <radialGradient id="matte" cx="50%" cy="40%" r="75%">
          <stop offset="0" stop-color="var(--ink-dark)"/>
          <stop offset="1" stop-color="var(--ink-deep)"/>
        </radialGradient>
      </defs>
      <rect width="540" height="309" fill="url(#matte)"/>
    </svg>
    <div class="back-brand">
      <span class="brand-mark"></span>
      <span class="brand-name">Dravelin Consulting Services</span>
    </div>
  </section>

</main>
</body>
</html>
```